R.T.Pell Logging Web design

Our website needs a redesign. We want it to appear professional and easy to navigate. We will be adding videos and pictures to the new website. We do not sell any products on our website. It should be designed for informational purposes. Our company performs timber harvesting and forest management services. Attached is our new company logo.

www.rtpelllogging-example.com if you want to see our current website.

Industry/Entity Type

Graphic Design

Coding

Coded - Design and coding required

```html
<!DOCTYPE html>
<html lang="en">
<head>
<meta charset="utf-8">
<title>R.T.Pell Logging Company</title>
<link href="https://fonts.googleapis.com/css2?family=Ubuntu:wght@400;500;700&family=Bree+Serif&display=swap" rel="stylesheet">
<style>
:root{
  --brown:#5a2e0e;
  --brown-dark:#3a1d0b;
  --gold:#e3ae42;
  --gold-light:#f0c25a;
  --grey-bg:#ededed;
  --text:#3c3c3c;
  --white:#fff;
}
*{margin:0;padding:0;box-sizing:border-box}
html,body{width:1006px;height:1200px;overflow:hidden;background:#fff}
body{font-family:'Ubuntu',sans-serif;color:var(--text);position:relative}
.abs{position:absolute}
.site-header{left:0;top:0;width:1006px;height:111px;border-top:2px solid var(--brown);border-bottom:2px solid var(--gold);background:#fff}
.brand{left:110px;top:25px;display:flex;align-items:center;gap:14px}
.brand-mark{width:50px;height:50px;background:var(--gold);border-radius:6px}
.brand-name{font-family:'Ubuntu',sans-serif;font-weight:700;font-size:30px;color:var(--brown);letter-spacing:0.5px;line-height:1}
.top-contact{right:110px;top:10px;font-size:12px;color:var(--brown);display:flex;gap:14px;align-items:center}
.top-contact span{display:flex;align-items:center;gap:5px}
.follow{right:109px;top:34px;display:flex;align-items:center;gap:5px;font-size:12px;color:var(--brown)}
.social{width:20px;height:20px;border-radius:50%;background:var(--gold)}
.main-nav{left:488px;top:64px;width:409px;height:27px;display:flex;background:var(--brown);box-shadow:0 6px 6px -4px rgba(0,0,0,.35)}
.main-nav a{color:#fff;text-decoration:none;font-size:12px;font-weight:500;display:flex;align-items:center;justify-content:center;border-left:1px solid #7a4a26}
.main-nav a.current{background:var(--gold);border-left:none}
.hero{left:0;top:111px;width:1006px;height:374px;background:linear-gradient(180deg,#6ea9d8 0%,#8fbfe3 14%,#b0693a 30%,#c98d55 55%,#7d4523 100%)}
.hero-caption{left:0;top:422px;width:1006px;height:63px;background:rgba(40,28,20,.72)}
.hero-caption p{position:absolute;left:118px;top:6px;color:#fff;font-size:20px;line-height:26px}
.dots{position:absolute;left:847px;top:40px;display:flex;gap:7px}
.dots i{width:9px;height:9px;border-radius:50%;border:1px solid #fff;display:block}
.dots i.on{background:#fff}
.welcome{left:0;top:485px;width:1006px;height:294px;background:var(--grey-bg)}
.welcome-mark{left:110px;top:517px;width:66px;height:56px;background:var(--gold);border-radius:8px;border:3px solid var(--brown)}
.welcome-title{left:185px;top:514px;font-family:'Bree Serif',serif;font-size:25px;line-height:28px;letter-spacing:.5px}
.welcome-title .l1{color:var(--brown)}
.welcome-title .l2{color:var(--gold)}
.rule{left:110px;top:583px;width:498px;height:1px;background:#d4d4d4}
.intro{left:110px;top:613px;width:498px;font-size:11px;line-height:16.3px;text-align:justify;color:#444}
.intro a{color:var(--brown);text-decoration:none;display:block}
.video{left:636px;top:585px;width:254px;height:160px;background:#1d1d1d;box-shadow:0 14px 10px -8px rgba(0,0,0,.35)}
.video-frame{position:absolute;left:6px;top:5px;width:242px;height:150px;background:linear-gradient(180deg,#7d8b6a,#5f7149 60%,#8a7a5a)}
.play{position:absolute;left:108px;top:52px;width:34px;height:34px;border-radius:50%;background:rgba(255,255,255,.6);border:2px solid #ddd}
.play:after{content:"";position:absolute;left:12px;top:8px;border-left:12px solid #444;border-top:7px solid transparent;border-bottom:7px solid transparent}
.controls{position:absolute;left:6px;top:131px;width:242px;height:23px;background:#111;color:#fff;font-size:9px;display:flex;align-items:center;gap:6px;padding:0 5px}
.track{flex:1;height:5px;background:#555;border-radius:3px}
.services{left:0;top:779px;width:1006px;height:309px;background:var(--gold);border-top:1px solid #f4d48d}
.services h2{position:absolute;left:0;top:28px;width:1006px;text-align:center;color:#fff;font-size:22px;font-weight:500;letter-spacing:.5px}
.services .srule{position:absolute;left:110px;top:68px;width:788px;height:1px;background:#f0c878}
.card{top:862px;width:378px;height:195px;border:2px solid #fff;overflow:hidden}
.card .photo{position:absolute;inset:0}
.card .caption{position:absolute;left:0;bottom:0;width:100%;height:70px;background:rgba(20,14,8,.6);color:#fff;padding:0 6px}
.card h3{position:absolute;left:5px;top:-22px;font-size:16px;font-weight:500;text-shadow:0 1px 2px #000}
.card .cline{position:absolute;left:5px;top:0;width:266px;height:1px;background:rgba(255,255,255,.5)}
.card p{position:absolute;left:5px;top:8px;width:366px;font-size:10.5px;line-height:15px}
.card p b{font-weight:700}
.site-footer{left:0;top:1088px;width:1006px;height:112px;background:var(--brown-dark)}
.foot-nav{position:absolute;left:113px;top:14px;color:#fff;font-size:12px;display:flex;gap:15px}
.foot-contact{position:absolute;left:110px;top:39px;color:#fff;font-size:12px;display:flex;gap:14px;align-items:center}
.foot-contact span{display:flex;align-items:center;gap:5px}
.subscribe{position:absolute;left:110px;top:67px;display:flex}
.subscribe .field{width:145px;height:26px;background:#fff;border-radius:3px 0 0 3px;font-size:10px;font-style:italic;color:#999;display:flex;align-items:center;gap:5px;padding-left:8px}
.subscribe .btn{width:76px;height:26px;background:var(--gold);color:#fff;font-size:11px;font-weight:700;display:flex;align-items:center;justify-content:center;border-radius:0 3px 3px 0}
.foot-mark{position:absolute;left:752px;top:15px;width:68px;height:56px;background:var(--gold);border-radius:8px}
.copy{position:absolute;right:114px;top:82px;color:#fff;font-size:11px}
</style>
</head>
<body>
<header class="site-header abs">
  <div class="brand abs"><div class="brand-mark"></div><div class="brand-name">R.T.PELL LOGGING</div></div>
  <div class="top-contact abs">
    <span><svg width="15" height="11" viewBox="0 0 15 11"><rect x=".5" y=".5" width="14" height="10" fill="none" stroke="#e3ae42"/><path d="M.5 .5 7.5 6 14.5 .5" fill="none" stroke="#e3ae42"/></svg>info@rtpellloggingcompany-example.com</span>
    <span><svg width="12" height="12" viewBox="0 0 12 12"><path d="M2 1l2 0 1 3-1.5 1a7 7 0 0 0 3.5 3.5L8 7l3 1v2a1 1 0 0 1-1 1A9 9 0 0 1 1 2a1 1 0 0 1 1-1z" fill="none" stroke="#e3ae42"/></svg>(555) 014-2290</span>
  </div>
  <div class="follow abs">Follow Us: <span class="social"></span><span class="social"></span><span class="social"></span></div>
  <nav class="main-nav abs">
    <a class="current" href="#" style="width:86px">HOME</a>
    <a href="#" style="width:99px">ABOUT US</a>
    <a href="#" style="width:107px">SERVICES</a>
    <a href="#" style="width:117px">CONTACT US</a>
  </nav>
</header>

<div class="hero abs" role="img" aria-label="Stacked freshly cut pine logs under a blue sky"></div>
<div class="hero-caption abs">
  <p>If you have a timber exemption on your property, call us.<br>We can write timber management plans for you.</p>
  <div class="dots"><i class="on"></i><i></i><i class="on"></i><i class="on"></i></div>
</div>

<section class="welcome abs"></section>
<div class="welcome-mark abs"></div>
<h1 class="welcome-title abs"><span class="l1">WELCOME TO</span><br><span class="l2">R.T.PELL LOGGING COMPANY</span></h1>
<div class="rule abs"></div>
<p class="intro abs">My name is Rob Pell and I started this company in 1999. I was born and raised in the piney woods of East Texas. Growing up, I spent most of my free time in the woods logging with my dad. I've been around this industry all my life. When I started this company, I set out to improve the harvesting experience for the property owner. Building on the standards set by my father, today, my company is proudly serving East Texas by providing professional timber harvesting and forest management services. My goal is to consitently exceed our customer's expectations. R.T.Pell Logging employees also take pride in keeping our customer's forest healthy. From start to finish, we always work to protect the forest and the environment. We look forward to earning your business.<a href="#">Read More »</a></p>
<div class="video abs">
  <div class="video-frame" role="img" aria-label="Video still of a pine forest with cut logs on the ground"></div>
  <div class="play"></div>
  <div class="controls"><svg width="8" height="9"><path d="M0 0 8 4.5 0 9z" fill="#fff"/></svg>04:59<div class="track"></div>10:35<svg width="10" height="9"><path d="M0 3h3l3-3v9L3 6H0z" fill="#fff"/></svg></div>
</div>

<section class="services abs">
  <h2>OUR SERVICES</h2>
  <div class="srule"></div>
</section>
<article class="card abs" style="left:109px">
  <div class="photo" role="img" aria-label="Log loader grapple lifting harvested timber" style="background:linear-gradient(180deg,#4f6a3a,#8a6a45 50%,#b88455)"></div>
  <div class="caption"><h3>Timber Harvesting</h3><div class="cline"></div><p>Lorem ipsum dolor sit amet, consectetuer adipiscing elit, sed diam nonummy nibh euismod tinciduntm ut laoreet dolore magna aliquam.. <b style="float:right">Read More&gt;&gt;</b></p></div>
</article>
<article class="card abs" style="left:521px">
  <div class="photo" role="img" aria-label="Forestry workers in hard hats walking through a forest" style="background:linear-gradient(180deg,#6f8158,#3f5230 60%,#2e3a22)"></div>
  <div class="caption"><h3>Forest Management</h3><div class="cline"></div><p>Lorem ipsum dolor sit amet, consectetuer adipiscing elit, sed diam nonummy nibh euismod tinciduntm ut laoreet dolore magna aliquam.. <b style="float:right">Read More&gt;&gt;</b></p></div>
</article>

<footer class="site-footer abs">
  <nav class="foot-nav"><span>HOME</span><span>|</span><span>ABOUT US</span><span>|</span><span>SERVICES</span><span>|</span><span>CONTACT US</span></nav>
  <div class="foot-contact">
    <span><svg width="16" height="14" viewBox="0 0 16 14"><path d="M1 7 8 1l7 6M3 6v7h4V9h2v4h4V6" fill="#fff" stroke="#fff"/></svg>Lorem ipsum dolor sit amet weriueirwoere</span>
    <span><svg width="15" height="11"><rect x=".5" y=".5" width="14" height="10" fill="none" stroke="#fff"/><path d="M.5 .5 7.5 6 14.5 .5" fill="none" stroke="#fff"/></svg>(555) 014-2290</span>
    <span><svg width="13" height="13" viewBox="0 0 13 13"><circle cx="6.5" cy="6.5" r="5.5" fill="none" stroke="#fff" stroke-width="1.3"/><circle cx="6.5" cy="6.5" r="2.3" fill="none" stroke="#fff" stroke-width="1.3"/></svg>info@rtpelllogging-example.com</span>
  </div>
  <div class="subscribe"><div class="field"><svg width="12" height="9"><rect x=".5" y=".5" width="11" height="8" fill="none" stroke="#bbb"/></svg>your e-mail address</div><div class="btn">SUBSCRIBE</div></div>
  <div class="foot-mark"></div>
  <div class="copy">© 2014 &nbsp;RTPellLogging. All Rights Reserved</div>
</footer>
</body>
</html>
```